A3 Poster Design for BUSINESS COACHING services

A3 Poster design for business coaching - we want it to be visual - minimal words. Needs to contain:
- our logo (uploaded)
- the words BUSINESS COACHING - Business or a Hobby? Talk to us today about our business coaching services to take your business to the next level
- and some graphics (open to ideas of something representative of coaching/working together/ improving business profits/success)
The poster will be physically in our business premises and will be more a cue for existing clients to ask us about a service they may not know we offer and so why it doesn't need to be informational

Target Market(s)

Small to Medium Business Owners

Industry/Entity Type

Small Business

Requirements
Must have
• Needs to contain:
• - our logo (uploaded)
• - the words BUSINESS COACHING - Business or a Hobby? Talk to us today about our business coaching services to take your business to the next level
• - and some graphics (open to ideas of something representative of coaching/working together/ improving business profits/success)

```html
<!DOCTYPE html>
<html lang="en">
<head>
<meta charset="utf-8">
<title>Business Coaching Poster</title>
<link href="https://fonts.googleapis.com/css2?family=Anton&family=Open+Sans:wght@700&display=swap" rel="stylesheet">
<style>
  :root {
    --backdrop: #ebebeb;
    --paper: #ffffff;
    --ink: #363638;
    --lime: #a6cf38;
    --lime-soft: #dbeea0;
    --pie-green: #5fb84a;
    --bar-green: #9ccd3d;
    --meeting-tone: #d9dcd6;
  }
  * { margin: 0; padding: 0; box-sizing: border-box; }
  html, body { width: 1200px; height: 1200px; overflow: hidden; background: var(--backdrop); }
  .poster {
    position: absolute; left: 198px; top: 38px; width: 803px; height: 1122px;
    background: linear-gradient(90deg, var(--lime-soft) 0, var(--paper) 36px, var(--paper) calc(100% - 36px), var(--lime-soft) 100%);
  }
  .headline-stack { position: absolute; inset: 0; }
  .headline-stack text { font-family: "Anton", "Impact", sans-serif; text-transform: uppercase; }
  .ink { fill: var(--ink); }
  .lime { fill: var(--lime); }
  .art { position: absolute; border-radius: 10px; }
  .art-meeting { left: 526px; top: 56px; width: 220px; height: 150px;
    background: radial-gradient(ellipse at 50% 55%, var(--meeting-tone), #f2f4ef 75%); }
  .art-pie { left: 78px; top: 552px; width: 236px; height: 210px;
    background: radial-gradient(ellipse at 50% 55%, var(--pie-green), #cfe9c4 80%); }
  .art-growth { left: 574px; top: 746px; width: 168px; height: 142px;
    background: linear-gradient(90deg, var(--lime-soft), var(--bar-green)); }
  .brand {
    position: absolute; left: 0; right: 0; top: 920px;
    display: flex; flex-direction: column; align-items: center; gap: 22px;
  }
  .brand-dot { width: 80px; height: 80px; border-radius: 50%; background: var(--lime); }
  .brand-name { font-family: "Open Sans", "Arial", sans-serif; font-weight: 700; font-size: 30px; color: var(--ink); letter-spacing: -0.5px; }
  .site-band {
    position: absolute; left: 0; right: 0; bottom: 0; height: 40px; background: var(--ink);
    display: flex; align-items: center; justify-content: center;
  }
  .site-url { font-family: "Open Sans", "Arial", sans-serif; font-weight: 700; font-size: 22px; color: var(--paper); }
</style>
</head>
<body>
  <main class="poster">
    <div class="art art-meeting" role="img" aria-label="Illustration of a business team meeting around a table"></div>
    <div class="art art-pie" role="img" aria-label="Illustration of a green pie chart with business people standing on its slices"></div>
    <div class="art art-growth" role="img" aria-label="Illustration of rising green bars with business people standing on top"></div>

    <svg class="headline-stack" viewBox="0 0 803 1122" width="803" height="1122">
      <text class="ink" x="128" y="100" font-size="55" textLength="288" lengthAdjust="spacingAndGlyphs">The Words</text>
      <text class="ink" x="66" y="208" font-size="122" textLength="436" lengthAdjust="spacingAndGlyphs">Business</text>
      <text class="ink" x="66" y="372" font-size="197" textLength="678" lengthAdjust="spacingAndGlyphs">Coaching</text>

      <text class="lime" x="66" y="452" font-size="76" textLength="302" lengthAdjust="spacingAndGlyphs">Business</text>
      <text class="lime" x="378" y="452" font-size="40" textLength="102" lengthAdjust="spacingAndGlyphs">or a</text>
      <text class="lime" x="498" y="452" font-size="76" textLength="248" lengthAdjust="spacingAndGlyphs">Hobby?</text>
      <text class="lime" x="66" y="528" font-size="68" textLength="670" lengthAdjust="spacingAndGlyphs">Talk to us today about</text>

      <text class="ink" x="336" y="594" font-size="59" textLength="398" lengthAdjust="spacingAndGlyphs">Our Business</text>
      <text class="ink" x="336" y="674" font-size="81" textLength="398" lengthAdjust="spacingAndGlyphs">Coaching</text>
      <text class="ink" x="336" y="752" font-size="84" textLength="400" lengthAdjust="spacingAndGlyphs">Services</text>

      <text class="lime" x="62" y="822" font-size="39" textLength="248" lengthAdjust="spacingAndGlyphs">To take your</text>
      <text class="lime" x="322" y="822" font-size="52" textLength="236" lengthAdjust="spacingAndGlyphs">Business</text>
      <text class="lime" x="66" y="888" font-size="37" textLength="124" lengthAdjust="spacingAndGlyphs">To the</text>
      <text class="lime" x="206" y="888" font-size="58" textLength="352" lengthAdjust="spacingAndGlyphs">Next Level</text>
    </svg>

    <div class="brand">
      <span class="brand-dot"></span>
      <span class="brand-name">Summit Ledger Advisory</span>
    </div>

    <footer class="site-band">
      <span class="site-url">www.summitledgeradvisory.com</span>
    </footer>
  </main>
</body>
</html>
```